Graphic Design Project

I need a much better graphic representative of my companies values then what is shown in the attached doc. I work for a recycled paper company and while my boss like the colored paper design, he wants the words to spell out TALK.

I need this ASAP for a meeting on March 13.

Target Market(s)

Internal employees

Industry/Entity Type

Graphic Design

Requirements
Must have
• Be colorful, have our logo and line up our values so that it says "TALK".

```html
<!DOCTYPE html>
<html lang="en">
<head>
<meta charset="utf-8">
<title>TALK — Company Values</title>
<link rel="stylesheet" href="https://fonts.googleapis.com/css2?family=Marcellus&display=swap">
<style>
  :root {
    --bg-core: #8f735d;
    --bg-edge: #6f5643;
    --paper-light: #f6e2b6;
    --paper-mid: #ecc98c;
    --paper-deep: #d9a462;
    --value-brown: #5a3322;
    --initial-green: #18773a;
    --brand-green: #1d7a3c;
    --badge-white: #ffffff;
    --shadow: rgba(60, 40, 28, 0.55);
  }
  html, body {
    margin: 0;
    padding: 0;
    overflow: hidden;
  }
  .canvas {
    position: relative;
    width: 1200px;
    height: 900px;
    overflow: hidden;
    background: radial-gradient(ellipse at 55% 45%, var(--bg-core) 0%, var(--bg-core) 45%, var(--bg-edge) 100%);
    font-family: "Marcellus", Georgia, serif;
  }
  .brand-plate {
    position: absolute;
    left: 0;
    top: 42px;
    width: 472px;
    height: 148px;
    background: var(--badge-white);
    display: flex;
    align-items: center;
    gap: 16px;
    padding-left: 30px;
    box-sizing: border-box;
  }
  .brand-dot {
    width: 34px;
    height: 34px;
    border-radius: 50%;
    background: var(--brand-green);
    flex: none;
  }
  .brand-name {
    color: var(--brand-green);
    font-size: 34px;
    line-height: 1.1;
    margin: 0;
    font-weight: 400;
  }
  .speech-bubble {
    position: absolute;
    left: 0;
    top: 0;
    width: 1200px;
    height: 900px;
  }
  .values {
    position: absolute;
    left: 378px;
    top: 312px;
    margin: 0;
    padding: 0;
    list-style: none;
  }
  .value {
    font-size: 58px;
    line-height: 77px;
    color: var(--value-brown);
    letter-spacing: 0.5px;
    text-shadow: 1px 1px 1px rgba(255, 245, 220, 0.6);
  }
  .value-initial {
    color: var(--initial-green);
    font-size: 64px;
  }
</style>
</head>
<body>
  <main class="canvas">
    <header class="brand-plate">
      <span class="brand-dot"></span>
      <p class="brand-name">Harlow Recycled<br>Board Co.</p>
    </header>

    <svg class="speech-bubble" viewBox="0 0 1200 900" aria-hidden="true">
      <defs>
        <linearGradient id="paperFill" x1="0" y1="0" x2="1" y2="1">
          <stop offset="0" stop-color="var(--paper-light)"/>
          <stop offset="0.55" stop-color="var(--paper-mid)"/>
          <stop offset="1" stop-color="var(--paper-deep)"/>
        </linearGradient>
        <radialGradient id="groundShadow">
          <stop offset="0" stop-color="var(--shadow)"/>
          <stop offset="1" stop-color="rgba(60,40,28,0)"/>
        </radialGradient>
      </defs>
      <ellipse cx="760" cy="762" rx="300" ry="20" fill="url(#groundShadow)"/>
      <path fill="url(#paperFill)"
        d="M298,300 L318,290 336,296 352,287 380,292 404,284 430,290 470,283 510,289 548,282
           590,288 640,281 690,287 740,280 790,286 840,281 880,287 902,284
           Q930,284 930,314 L930,612 Q930,640 914,648 L996,762 L846,642 L318,642
           Q296,642 296,620 L292,590 298,560 289,530 297,500 290,470 298,440
           289,410 296,380 288,350 296,325 Z"/>
    </svg>

    <ul class="values">
      <li class="value"><span class="value-initial">T</span>eamwork</li>
      <li class="value"><span class="value-initial">A</span>ccountability</li>
      <li class="value"><span class="value-initial">L</span>eadership</li>
      <li class="value"><span class="value-initial">K</span>nowledge</li>
    </ul>
  </main>
</body>
</html>
```